Powerpoint design template for PLAYNOVA for new digital platform

We would like to use a PowerPoint template, we would like to create a new page, we would like to create a new digital platform PLAYNOVA for schools and parents for the creation of playful communication and educational tools for children to enhance their positive development, amaze them learn in a playful way. This platform is going to be the most creative, stimulating and innovative classroom, easy to use and fast to implement. Scrapbooking, collages ... Magazine, newsletters Diplomla / awards Slideshows Facebook Calendars Organizers Greetings Games ... This powerpoint template will be used essential to We are looking for a professional design, positioning our brand in the children market with an adult hearing. so you will need to find a good deal. Primary target: nurseries & schools from 0 to 18 years old and universities (in 2nd phase) Secondary target: small & medium businesses Third target: general public, and TPE If it is a color scheme, then it is suggested that it be marketed in Europe (UK, Italy, Spain) and in a 2nd Stage USA and other countries. multiple options for front page, insidious pages (multiple styles with limited text and extended text) and final contact page We need something to read, we can not do it too much, but we can not do it. , and inside pages aligned to our logo

Target Market(s)

Target 1; Education with teacher Target 2; parents and grandparents

Industry/Entity Type

Education

Font styles to use
Other font styles liked:
• not decided. but not too fancy

Requirements
Must have
• Multi page options for front page, page insides (multiple styles with limited text and extended text) and final page contact
Nice to have
• do not have a lot of ideas. We need something to read, we can not get away from it
Should not have
• not too fancy and busy: keep clarity & simplicity while reassuring on quality

```html
<!DOCTYPE html>
<html lang="en">
<head>
<meta charset="utf-8">
<title>PLAYNOVA – Presentation Template Overview</title>
<link rel="stylesheet" href="https://fonts.googleapis.com/css2?family=Poppins:wght@400;600;800&display=swap">
<style>
:root{
  --lime:#c3d62b;
  --lime-soft:#e4ee9a;
  --teal:#27b3c4;
  --pink:#e8367c;
  --orange:#f7941d;
  --purple:#8c5fb8;
  --ink:#4a4a4a;
  --grey:#8a8a8a;
  --line:#e3e3e3;
  --paper:#ffffff;
  --canvas:#eeeeee;
}
*{box-sizing:border-box;margin:0;padding:0}
html,body{width:1200px;height:3516px;overflow:hidden;background:var(--canvas)}
body{font-family:"Poppins",sans-serif;color:var(--ink)}
.deck{width:1200px;height:3516px;padding:4px;display:grid;grid-template-columns:repeat(3,1fr);grid-template-rows:repeat(16,1fr);gap:5px}
.slide{position:relative;background:var(--paper);overflow:hidden}
.slide::after{content:"";position:absolute;left:0;right:0;bottom:0;height:7px;background:var(--lime)}
.slide.nobar::after{display:none}
.title{position:absolute;left:14px;top:12px;font-weight:600;font-size:12px;color:var(--teal);white-space:nowrap}
.title.lg{font-size:17px;line-height:1.1;white-space:normal}
.brand{position:absolute;right:12px;top:10px;font-weight:800;font-size:9px;color:var(--pink);display:flex;align-items:center;gap:3px}
.brand::before{content:"";width:7px;height:7px;border-radius:50%;background:var(--lime)}
.ph{position:absolute;background:linear-gradient(135deg,#f4d7bb,#a9cfe0)}
.ph.warm{background:linear-gradient(135deg,#f7dcc3,#e9b99a)}
.ph.cool{background:linear-gradient(135deg,#cfe5ee,#8dbfd3)}
.ph.green{background:linear-gradient(135deg,#e6efb0,#aac63a)}
.ph.dark{background:linear-gradient(135deg,#3a3a3a,#151515)}
.ph.mix{background:linear-gradient(135deg,#f6c2d4,#f9d98c,#a9e0e8)}
.t{position:absolute;font-size:5px;line-height:1.55;color:var(--grey)}
.h{position:absolute;font-weight:600;font-size:7px;color:var(--ink);white-space:nowrap}
.ic{position:absolute;width:14px;height:14px;border-radius:50%;background:var(--teal)}
.box{position:absolute}
.c-lime{background:var(--lime)}.c-teal{background:var(--teal)}.c-pink{background:var(--pink)}.c-orange{background:var(--orange)}.c-purple{background:var(--purple)}
.w{color:#fff}
.rule{position:absolute;height:1px;background:var(--line)}
.big-brand{position:absolute;font-weight:800;color:var(--pink);display:flex;align-items:center;gap:6px}
.big-brand::before{content:"";width:18px;height:18px;border-radius:50%;background:var(--lime)}
</style>
</head>
<body>
<main class="deck">

<!-- Row 1 -->
<section class="slide cover">
  <div class="box c-lime" style="left:0;top:150px;width:394px;height:64px;opacity:.35"></div>
  <div class="big-brand" style="left:40px;top:70px;font-size:34px">PLAYNOVA</div>
  <div class="t" style="left:72px;top:118px;font-size:7px;color:var(--ink)">Playful tools for schools and parents</div>
  <div class="t" style="left:72px;top:128px">Presentation template</div>
</section>
<section class="slide">
  <div class="ph warm" role="img" aria-label="Photo of children learning together" style="left:0;top:0;width:394px;height:214px"></div>
  <div class="box c-lime" style="left:110px;top:88px;width:174px;height:40px"></div>
  <div class="h w" style="left:128px;top:96px;font-size:11px">Your Title Goes Here</div>
  <div class="t w" style="left:150px;top:114px">Short subtitle line</div>
</section>
<section class="slide">
  <div class="ph" role="img" aria-label="Photo of a smiling child in class" style="left:0;top:0;width:394px;height:214px"></div>
  <div class="box c-lime" style="left:200px;top:60px;width:170px;height:40px"></div>
  <div class="h w" style="left:214px;top:68px;font-size:11px">Your Title Goes Here</div>
  <div class="t w" style="left:236px;top:86px">Short subtitle line</div>
</section>

<!-- Row 2 -->
<section class="slide">
  <div class="title">Our Agenda</div><div class="brand">PLAYNOVA</div>
  <div class="ic c-teal" style="left:22px;top:50px"></div><div class="h" style="left:42px;top:52px">Introduction</div>
  <div class="ic c-pink" style="left:22px;top:85px"></div><div class="h" style="left:42px;top:87px">Our Services</div>
  <div class="ic c-orange" style="left:22px;top:120px"></div><div class="h" style="left:42px;top:122px">Portfolio</div>
  <div class="ic c-lime" style="left:150px;top:50px"></div><div class="h" style="left:170px;top:52px">Our Team</div>
  <div class="ic c-purple" style="left:150px;top:85px"></div><div class="h" style="left:170px;top:87px">Pricing</div>
  <div class="ic c-teal" style="left:150px;top:120px"></div><div class="h" style="left:170px;top:122px">Contact</div>
  <div class="box c-lime" style="left:270px;top:40px;width:110px;height:120px;opacity:.35;clip-path:polygon(50% 0,100% 50%,50% 100%,0 50%)"></div>
</section>
<section class="slide">
  <div class="ph cool" role="img" aria-label="Banner photo of a classroom" style="left:0;top:0;width:394px;height:42px"></div>
  <div class="title" style="top:54px">Our Vision &amp; Mission</div>
  <div class="h" style="left:14px;top:80px;color:var(--pink)">Vision</div>
  <div class="t" style="left:14px;top:92px;width:170px">We help children learn with joy and wonder, giving teachers simple tools that spark curiosity every day.</div>
  <div class="h" style="left:210px;top:80px;color:var(--teal)">Mission</div>
  <div class="t" style="left:210px;top:92px;width:170px">We build creative classroom resources that are easy to use, fast to set up and loved by every family.</div>
</section>
<section class="slide">
  <div class="title">Our Services</div><div class="brand">PLAYNOVA</div>
  <div class="ph warm" role="img" aria-label="Photo of a teacher with pupils" style="left:14px;top:40px;width:120px;height:80px"></div>
  <div class="ph cool" role="img" aria-label="Photo of children painting" style="left:14px;top:124px;width:120px;height:70px"></div>
  <div class="h" style="left:150px;top:44px">Creative Tools</div>
  <div class="t" style="left:150px;top:56px;width:230px">Collages, newsletters and awards made in minutes for any class.</div>
  <div class="h" style="left:150px;top:90px">Calendars &amp; Games</div>
  <div class="t" style="left:150px;top:102px;width:230px">Playful organizers that keep pupils and parents on track.</div>
  <div class="h" style="left:150px;top:136px">Slideshows</div>
  <div class="t" style="left:150px;top:148px;width:230px">Share lessons and school moments with bright visual stories.</div>
</section>

<!-- Row 3 -->
<section class="slide">
  <div class="ph warm" role="img" aria-label="Photo of a teacher reading to a girl" style="left:0;top:0;width:240px;height:214px"></div>
  <div class="box c-lime" style="left:240px;top:0;width:154px;height:214px"></div>
  <div class="h w" style="left:256px;top:80px;font-size:11px">Your Title</div>
  <div class="t w" style="left:256px;top:98px;width:124px">Short text that introduces this chapter of the talk.</div>
</section>
<section class="slide">
  <div class="title">Your Title</div><div class="brand">PLAYNOVA</div>
  <div class="ph" role="img" aria-label="Photo of a girl holding books" style="left:14px;top:38px;width:150px;height:158px"></div>
  <div class="ic c-teal" style="left:180px;top:50px"></div><div class="t" style="left:200px;top:52px;width:180px">Clear goals for every learning step.</div>
  <div class="ic c-pink" style="left:180px;top:85px"></div><div class="t" style="left:200px;top:87px;width:180px">Activities that grow confidence.</div>
  <div class="ic c-orange" style="left:180px;top:120px"></div><div class="t" style="left:200px;top:122px;width:180px">Feedback that parents understand.</div>
  <div class="ic c-lime" style="left:180px;top:155px"></div><div class="t" style="left:200px;top:157px;width:180px">Results shared with the whole school.</div>
</section>
<section class="slide">
  <div class="ph cool" role="img" aria-label="Photo of children working at desks" style="left:0;top:0;width:394px;height:214px"></div>
  <div class="box" style="left:20px;top:60px;width:150px;height:90px;background:rgba(255,255,255,.9)"></div>
  <div class="h" style="left:32px;top:74px;color:var(--teal);font-size:10px">Your Title Here</div>
  <div class="t" style="left:32px;top:92px;width:126px">Short supporting text for this image slide.</div>
</section>

<!-- Row 4 -->
<section class="slide">
  <div class="ph warm" role="img" aria-label="Photo of a mother and daughter" style="left:0;top:0;width:170px;height:214px"></div>
  <div class="title lg" style="left:190px;top:60px;width:180px">Your Title Goes Here</div>
  <div class="t" style="left:190px;top:106px;width:180px">Add a short description of the topic that follows on the next slides.</div>
</section>
<section class="slide">
  <div class="box c-lime" style="left:0;top:0;width:394px;height:214px;opacity:.85"></div>
  <div class="box" style="left:180px;top:40px;width:34px;height:34px;border-radius:50%;background:#fff"></div>
  <div class="h" style="left:190px;top:42px;font-size:22px;color:var(--lime)">“</div>
  <div class="t w" style="left:60px;top:92px;width:274px;text-align:center;font-size:7px">Learning is most powerful when it feels like play, and every child deserves that joy.</div>
  <div class="h w" style="left:170px;top:130px">Jane Doe</div>
</section>
<section class="slide">
  <div class="title">Quote Area</div><div class="brand">PLAYNOVA</div>
  <div class="t" style="left:14px;top:50px;width:190px;font-size:7px;color:var(--ink)">“A school that plays together learns together and grows together.”</div>
  <div class="h" style="left:14px;top:90px;color:var(--pink)">Anna Brook</div>
  <div class="ph" role="img" aria-label="Photo of a smiling girl" style="left:230px;top:0;width:164px;height:207px"></div>
</section>

<!-- Row 5 -->
<section class="slide">
  <div class="title">Your Title Goes Here</div><div class="brand">PLAYNOVA</div>
  <div class="h" style="left:14px;top:44px">Welcome to class</div>
  <div class="t" style="left:14px;top:56px;width:150px">Short paragraph about our approach to teaching with joy and care.</div>
  <div class="ph warm" role="img" aria-label="Photo of pupils" style="left:14px;top:100px;width:70px;height:60px"></div>
  <div class="ph cool" role="img" aria-label="Photo of a teacher" style="left:90px;top:100px;width:70px;height:60px"></div>
  <div class="ph" role="img" aria-label="Photo of children at play" style="left:190px;top:44px;width:190px;height:150px"></div>
</section>
<section class="slide">
  <div class="title">Our Differences</div><div class="brand">PLAYNOVA</div>
  <div class="ic c-teal" style="left:40px;top:60px;width:30px;height:30px"></div>
  <div class="ic c-pink" style="left:140px;top:60px;width:30px;height:30px"></div>
  <div class="ic c-orange" style="left:240px;top:60px;width:30px;height:30px"></div>
  <div class="ic c-lime" style="left:330px;top:60px;width:30px;height:30px"></div>
  <div class="t" style="left:24px;top:102px;width:70px">Simple tools for busy teachers.</div>
  <div class="t" style="left:124px;top:102px;width:70px">Safe space for young minds.</div>
  <div class="t" style="left:224px;top:102px;width:70px">Fresh ideas every month.</div>
  <div class="t" style="left:314px;top:102px;width:70px">Support close to schools.</div>
</section>
<section class="slide">
  <div class="title">Your Title Goes Here</div><div class="brand">PLAYNOVA</div>
  <div class="t" style="left:14px;top:44px;width:160px">Introduce this topic with two or three lines of clear text.</div>
  <div class="box c-teal" style="left:200px;top:44px;width:180px;height:30px"></div><div class="h w" style="left:210px;top:55px">Option One</div>
  <div class="box c-pink" style="left:200px;top:80px;width:180px;height:30px"></div><div class="h w" style="left:210px;top:91px">Option Two</div>
  <div class="box c-orange" style="left:200px;top:116px;width:180px;height:30px"></div><div class="h w" style="left:210px;top:127px">Option Three</div>
  <div class="box c-lime" style="left:200px;top:152px;width:180px;height:30px"></div><div class="h w" style="left:210px;top:163px">Option Four</div>
</section>

<!-- Row 6 -->
<section class="slide">
  <div class="title">Text Area</div><div class="brand">PLAYNOVA</div>
  <div class="h" style="left:14px;top:40px">Your headline text here</div>
  <div class="t" style="left:14px;top:54px;width:366px">Our platform gives schools and parents playful ways to share news, celebrate progress and plan the week. Each tool is easy to learn and fast to use, so teachers spend more time with children and less time on paperwork. Families stay close to what happens in class.</div>
  <div class="t" style="left:14px;top:104px;width:366px">Create newsletters, diplomas, calendars and slideshows with bright layouts made for young learners. Every design is ready to print or share online in minutes.</div>
  <div class="t" style="left:14px;top:140px;width:366px">Start with a template, add your photos and words, and send it to the whole class.</div>
</section>
<section class="slide">
  <div class="ph green" role="img" aria-label="Diamond framed photo of a girl with a book" style="left:100px;top:10px;width:194px;height:194px;clip-path:polygon(50% 0,100% 50%,50% 100%,0 50%)"></div>
  <div class="ph warm" role="img" aria-label="Photo of children reading" style="left:0;top:0;width:90px;height:207px"></div>
  <div class="ph cool" role="img" aria-label="Photo of a classroom" style="left:304px;top:0;width:90px;height:207px"></div>
</section>
<section class="slide">
  <div class="title">Text Area</div><div class="brand">PLAYNOVA</div>
  <div class="t" style="left:14px;top:44px;width:200px">Add a short text about a key idea and how it helps children grow with care.</div>
  <div class="t" style="left:14px;top:80px;width:200px">Keep lines short so the slide stays clear and easy to read from afar.</div>
  <div class="ph" role="img" aria-label="Photo of a smiling girl" style="left:230px;top:30px;width:150px;height:164px"></div>
</section>

<!-- Row 7 -->
<section class="slide">
  <div class="ph mix" role="img" aria-label="Collage of colourful classroom photos" style="left:0;top:0;width:200px;height:207px"></div>
  <div class="title lg" style="left:214px;top:60px;width:170px">Your Title Goes Here</div>
  <div class="t" style="left:214px;top:104px;width:170px">A short intro for the gallery of moments.</div>
</section>
<section class="slide">
  <div class="title">Your Title Goes Here</div><div class="brand">PLAYNOVA</div>
  <div class="ph warm" role="img" aria-label="Photo of pupils" style="left:14px;top:40px;width:86px;height:70px"></div>
  <div class="ph cool" role="img" aria-label="Photo of pupils" style="left:106px;top:40px;width:86px;height:70px"></div>
  <div class="ph" role="img" aria-label="Photo of pupils" style="left:198px;top:40px;width:86px;height:70px"></div>
  <div class="ph green" role="img" aria-label="Photo of pupils" style="left:290px;top:40px;width:90px;height:70px"></div>
  <div class="t" style="left:14px;top:120px;width:86px">Art class fun.</div>
  <div class="t" style="left:106px;top:120px;width:86px">Reading time.</div>
  <div class="t" style="left:198px;top:120px;width:86px">Science day.</div>
  <div class="t" style="left:290px;top:120px;width:86px">Music hour.</div>
</section>
<section class="slide">
  <div class="title">Portfolio Area</div><div class="brand">PLAYNOVA</div>
  <div class="t" style="left:14px;top:44px;width:150px">Show the work your class is proud of with short captions.</div>
  <div class="ph warm" role="img" aria-label="Photo of a girl drawing" style="left:180px;top:38px;width:96px;height:78px"></div>
  <div class="ph cool" role="img" aria-label="Photo of a boy smiling" style="left:284px;top:38px;width:96px;height:78px"></div>
  <div class="ph" role="img" aria-label="Photo of kids outdoors" style="left:180px;top:120px;width:200px;height:76px"></div>
</section>

<!-- Row 8 -->
<section class="slide">
  <div class="title">Your Website Showcase</div><div class="brand">PLAYNOVA</div>
  <div class="h" style="left:14px;top:44px">Welcome online</div>
  <div class="t" style="left:14px;top:56px;width:170px">Parents can see news, photos and dates on one simple page built for families.</div>
  <div class="box" style="left:210px;top:44px;width:170px;height:110px;border:5px solid #333;border-radius:4px"></div>
  <div class="ph cool" role="img" aria-label="Website screenshot" style="left:215px;top:49px;width:160px;height:100px"></div>
  <div class="box" style="left:280px;top:154px;width:30px;height:14px;background:#333"></div>
</section>
<section class="slide">
  <div class="ph" role="img" aria-label="Photo of happy children jumping" style="left:0;top:0;width:394px;height:214px"></div>
  <div class="box" style="left:40px;top:70px;width:130px;height:70px;background:rgba(255,255,255,.9)"></div>
  <div class="h" style="left:52px;top:84px;color:var(--pink);font-size:10px">Big Moments</div>
  <div class="t" style="left:52px;top:102px;width:110px">A caption for this full photo.</div>
</section>
<section class="slide">
  <div class="title">Text Create Description</div><div class="brand">PLAYNOVA</div>
  <div class="t" style="left:14px;top:44px;width:115px">Describe the first step of the process here.</div>
  <div class="t" style="left:140px;top:44px;width:115px">Describe the second step of the process.</div>
  <div class="t" style="left:266px;top:44px;width:115px">Describe the final step and its results.</div>
  <div class="ph warm" role="img" aria-label="Photo of a teacher with kids" style="left:14px;top:90px;width:366px;height:104px"></div>
</section>

<!-- Row 9 -->
<section class="slide">
  <div class="ph green" role="img" aria-label="Photo of a girl with a laptop" style="left:0;top:0;width:150px;height:207px"></div>
  <div class="title lg" style="left:160px;top:30px;width:100px">Your Title Goes Here</div>
  <div class="ph warm" role="img" aria-label="Photo of a boy" style="left:270px;top:20px;width:110px;height:80px"></div>
  <div class="ph cool" role="img" aria-label="Photo of a class" style="left:270px;top:106px;width:110px;height:88px"></div>
  <div class="t" style="left:160px;top:90px;width:100px">Short text about this pair of photos.</div>
</section>
<section class="slide nobar">
  <div class="box" style="left:0;top:0;width:394px;height:214px;background:#f4f4f4"></div>
  <div class="ph dark" role="img" aria-label="Dark tablet device mockup" style="left:110px;top:30px;width:180px;height:150px;transform:rotate(-8deg)"></div>
  <div class="h" style="left:176px;top:186px;color:var(--lime)">PLAYNOVA</div>
</section>
<section class="slide">
  <div class="title">Your Title Goes Here</div><div class="brand">PLAYNOVA</div>
  <div class="ph" role="img" aria-label="Photo of kids laughing" style="left:14px;top:38px;width:170px;height:156px"></div>
  <div class="ic c-teal" style="left:200px;top:50px"></div><div class="t" style="left:220px;top:52px;width:160px">Plan lessons with ease.</div>
  <div class="ic c-pink" style="left:200px;top:90px"></div><div class="t" style="left:220px;top:92px;width:160px">Share news with parents.</div>
  <div class="ic c-orange" style="left:200px;top:130px"></div><div class="t" style="left:220px;top:132px;width:160px">Celebrate every success.</div>
</section>

<!-- Row 10 -->
<section class="slide">
  <div class="title">Icon Bullets with Paragraph</div><div class="brand">PLAYNOVA</div>
  <div class="ic c-teal" style="left:14px;top:48px"></div><div class="t" style="left:34px;top:48px;width:150px">Bright tools that make each day easier.</div>
  <div class="ic c-pink" style="left:14px;top:90px"></div><div class="t" style="left:34px;top:90px;width:150px">Games that build skills step by step.</div>
  <div class="ic c-orange" style="left:14px;top:132px"></div><div class="t" style="left:34px;top:132px;width:150px">Awards that make children proud.</div>
  <div class="ic c-lime" style="left:200px;top:48px"></div><div class="t" style="left:220px;top:48px;width:160px">Calendars shared with families.</div>
  <div class="ic c-purple" style="left:200px;top:90px"></div><div class="t" style="left:220px;top:90px;width:160px">Newsletters ready in minutes.</div>
  <div class="ic c-teal" style="left:200px;top:132px"></div><div class="t" style="left:220px;top:132px;width:160px">Slideshows for school events.</div>
</section>
<section class="slide">
  <div class="title">Pictures with Bullets</div><div class="brand">PLAYNOVA</div>
  <div class="ph mix" role="img" aria-label="Strip of children photos" style="left:14px;top:38px;width:366px;height:60px"></div>
  <div class="t" style="left:14px;top:110px;width:115px">• Learn by doing<br>• Play together</div>
  <div class="t" style="left:140px;top:110px;width:115px">• Share ideas<br>• Grow skills</div>
  <div class="t" style="left:266px;top:110px;width:115px">• Stay curious<br>• Have fun</div>
</section>
<section class="slide">
  <div class="title">Text &amp; Icon Area</div><div class="brand">PLAYNOVA</div>
  <div class="t" style="left:14px;top:44px;width:150px">A short overview of the main features for teachers and parents.</div>
  <div class="ic c-teal" style="left:190px;top:44px"></div><div class="t" style="left:210px;top:46px;width:170px">Easy to use</div>
  <div class="ic c-pink" style="left:190px;top:74px"></div><div class="t" style="left:210px;top:76px;width:170px">Fast to implement</div>
  <div class="ic c-orange" style="left:190px;top:104px"></div><div class="t" style="left:210px;top:106px;width:170px">Creative designs</div>
  <div class="ic c-lime" style="left:190px;top:134px"></div><div class="t" style="left:210px;top:136px;width:170px">Safe for children</div>
  <div class="ic c-purple" style="left:190px;top:164px"></div><div class="t" style="left:210px;top:166px;width:170px">Loved by families</div>
</section>

<!-- Row 11 -->
<section class="slide">
  <div class="title">Paragraph with Photo Bullet</div><div class="brand">PLAYNOVA</div>
  <div class="t" style="left:14px;top:40px;width:366px">Use this layout to explain three ideas, each with a small photo and a few lines of text.</div>
  <div class="ph warm" role="img" aria-label="Round photo of a child" style="left:40px;top:70px;width:50px;height:50px;border-radius:50%"></div>
  <div class="ph cool" role="img" aria-label="Round photo of a child" style="left:172px;top:70px;width:50px;height:50px;border-radius:50%"></div>
  <div class="ph" role="img" aria-label="Round photo of a child" style="left:304px;top:70px;width:50px;height:50px;border-radius:50%"></div>
  <div class="t" style="left:14px;top:130px;width:110px;text-align:center">Short idea text.</div>
  <div class="t" style="left:142px;top:130px;width:110px;text-align:center">Short idea text.</div>
  <div class="t" style="left:274px;top:130px;width:110px;text-align:center">Short idea text.</div>
</section>
<section class="slide">
  <div class="brand">PLAYNOVA</div>
  <div class="ph green" role="img" aria-label="Photo of a boy with a tablet" style="left:0;top:0;width:170px;height:207px"></div>
  <div class="h" style="left:186px;top:40px;color:var(--teal);font-size:10px">Portfolio Text</div>
  <div class="ic c-teal" style="left:186px;top:70px"></div><div class="t" style="left:206px;top:72px;width:170px">Project one summary.</div>
  <div class="ic c-pink" style="left:186px;top:104px"></div><div class="t" style="left:206px;top:106px;width:170px">Project two summary.</div>
  <div class="ic c-orange" style="left:186px;top:138px"></div><div class="t" style="left:206px;top:140px;width:170px">Project three summary.</div>
</section>
<section class="slide">
  <div class="title">Portfolio Content Area</div><div class="brand">PLAYNOVA</div>
  <div class="ph warm" role="img" aria-label="Photo of pupils" style="left:14px;top:40px;width:120px;height:80px"></div>
  <div class="ph cool" role="img" aria-label="Photo of a teacher" style="left:14px;top:124px;width:120px;height:70px"></div>
  <div class="h" style="left:150px;top:44px">Our Projects</div>
  <div class="t" style="left:150px;top:56px;width:230px">Examples of how schools use our tools in class and at home.</div>
  <div class="rule" style="left:150px;top:80px;width:230px"></div>
  <div class="t" style="left:150px;top:88px;width:230px">• Class newsletter<br>• Spring diploma<br>• Family calendar<br>• School slideshow</div>
</section>

<!-- Row 12 -->
<section class="slide">
  <div class="title">Your Title Goes Here</div><div class="brand">PLAYNOVA</div>
  <div class="ph cool" role="img" aria-label="Photo of kids in class" style="left:14px;top:38px;width:180px;height:156px"></div>
  <div class="ph warm" role="img" aria-label="Photo of a teacher and pupil" style="left:200px;top:38px;width:180px;height:76px"></div>
  <div class="t" style="left:200px;top:124px;width:180px">Short text about how our classrooms feel.</div>
</section>
<section class="slide">
  <div class="title">Global Experience</div><div class="brand">PLAYNOVA</div>
  <div class="ph" role="img" aria-label="World map showing countries served" style="left:14px;top:38px;width:250px;height:150px;background:linear-gradient(135deg,#dcdcdc,#c4c4c4)"></div>
  <div class="h" style="left:280px;top:50px;color:var(--pink)">Europe</div><div class="t" style="left:280px;top:62px">UK, Italy, Spain</div>
  <div class="h" style="left:280px;top:90px;color:var(--teal)">Next</div><div class="t" style="left:280px;top:102px">USA and more</div>
</section>
<section class="slide">
  <div class="title lg" style="top:40px;width:150px">Online Title Goes Here</div><div class="brand">PLAYNOVA</div>
  <div class="t" style="left:14px;top:90px;width:150px">Tell visitors about the online space for classes.</div>
  <div class="box" style="left:180px;top:36px;width:200px;height:130px;border:6px solid #ddd;border-radius:4px"></div>
  <div class="ph warm" role="img" aria-label="Screen showing a photo of a girl" style="left:186px;top:42px;width:188px;height:118px"></div>
  <div class="box" style="left:260px;top:166px;width:40px;height:16px;background:#ddd"></div>
</section>

<!-- Row 13 -->
<section class="slide">
  <div class="title">Text Column Area</div><div class="brand">PLAYNOVA</div>
  <div class="box c-teal" style="left:14px;top:40px;width:84px;height:150px"></div>
  <div class="box c-pink" style="left:106px;top:40px;width:84px;height:150px"></div>
  <div class="box c-orange" style="left:198px;top:40px;width:84px;height:150px"></div>
  <div class="box c-lime" style="left:290px;top:40px;width:90px;height:150px"></div>
  <div class="t w" style="left:22px;top:60px;width:70px">Column text for point one.</div>
  <div class="t w" style="left:114px;top:60px;width:70px">Column text for point two.</div>
  <div class="t w" style="left:206px;top:60px;width:70px">Column text for point three.</div>
  <div class="t w" style="left:298px;top:60px;width:76px">Column text for point four.</div>
</section>
<section class="slide">
  <div class="title">Text Column Area</div><div class="brand">PLAYNOVA</div>
  <div class="ic c-teal" style="left:40px;top:50px;width:30px;height:30px"></div>
  <div class="ic c-pink" style="left:132px;top:50px;width:30px;height:30px"></div>
  <div class="ic c-orange" style="left:224px;top:50px;width:30px;height:30px"></div>
  <div class="ic c-lime" style="left:316px;top:50px;width:30px;height:30px"></div>
  <div class="t" style="left:20px;top:96px;width:76px;text-align:center">Plan the week.</div>
  <div class="t" style="left:112px;top:96px;width:76px;text-align:center">Teach with play.</div>
  <div class="t" style="left:204px;top:96px;width:76px;text-align:center">Share results.</div>
  <div class="t" style="left:296px;top:96px;width:76px;text-align:center">Celebrate growth.</div>
</section>
<section class="slide">
  <div class="title">Text Points Area</div><div class="brand">PLAYNOVA</div>
  <div class="ic c-teal" style="left:30px;top:60px;width:40px;height:40px"></div>
  <div class="ic c-pink" style="left:105px;top:60px;width:40px;height:40px"></div>
  <div class="ic c-orange" style="left:180px;top:60px;width:40px;height:40px"></div>
  <div class="ic c-lime" style="left:255px;top:60px;width:40px;height:40px"></div>
  <div class="ic c-purple" style="left:330px;top:60px;width:40px;height:40px"></div>
  <div class="t" style="left:20px;top:112px;width:360px;text-align:center">Five key points, each explained with a short line below the icon.</div>
</section>

<!-- Row 14 -->
<section class="slide">
  <div class="title">Process Area</div><div class="brand">PLAYNOVA</div>
  <svg class="box" style="left:14px;top:50px" width="366" height="130" viewBox="0 0 366 130">
    <g font-family="Poppins,sans-serif" font-size="7" fill="#fff">
      <rect x="0" y="50" width="70" height="26" fill="#27b3c4"/><text x="12" y="66">Idea</text>
      <rect x="100" y="10" width="70" height="26" fill="#e8367c"/><text x="112" y="26">Design</text>
      <rect x="100" y="90" width="70" height="26" fill="#f7941d"/><text x="112" y="106">Review</text>
      <rect x="200" y="50" width="70" height="26" fill="#c3d62b"/><text x="212" y="66">Build</text>
      <rect x="296" y="50" width="70" height="26" fill="#8c5fb8"/><text x="308" y="66">Share</text>
    </g>
    <g stroke="#aaa" fill="none">
      <path d="M70 63H85V23H100M85 63V103H100M170 23H185V63H200M170 103H185V63M270 63H296"/>
    </g>
  </svg>
</section>
<section class="slide">
  <div class="title">Workflow Area</div><div class="brand">PLAYNOVA</div>
  <svg class="box" style="left:14px;top:60px" width="366" height="110" viewBox="0 0 366 110" fill="none" stroke-width="10">
    <path d="M10 60a36 36 0 0 1 72 0" stroke="#27b3c4"/>
    <path d="M82 60a36 36 0 0 0 72 0" stroke="#e8367c"/>
    <path d="M154 60a36 36 0 0 1 72 0" stroke="#f7941d"/>
    <path d="M226 60a36 36 0 0 0 72 0" stroke="#c3d62b"/>
    <path d="M298 60a30 30 0 0 1 60 0" stroke="#8c5fb8"/>
  </svg>
  <div class="t" style="left:24px;top:180px">Step 1</div><div class="t" style="left:100px;top:180px">Step 2</div><div class="t" style="left:172px;top:180px">Step 3</div><div class="t" style="left:244px;top:180px">Step 4</div><div class="t" style="left:318px;top:180px">Step 5</div>
</section>
<section class="slide">
  <div class="title">Timeline</div><div class="brand">PLAYNOVA</div>
  <div class="rule" style="left:20px;top:110px;width:354px;height:2px;background:#ccc"></div>
  <div class="ic c-teal" style="left:40px;top:96px;width:28px;height:28px"></div>
  <div class="ic c-pink" style="left:120px;top:96px;width:28px;height:28px"></div>
  <div class="ic c-orange" style="left:200px;top:96px;width:28px;height:28px"></div>
  <div class="ic c-lime" style="left:280px;top:96px;width:28px;height:28px"></div>
  <div class="t" style="left:36px;top:70px">2020</div><div class="t" style="left:116px;top:136px">2021</div><div class="t" style="left:196px;top:70px">2022</div><div class="t" style="left:276px;top:136px">2023</div>
</section>

<!-- Row 15 -->
<section class="slide">
  <div class="title">Radial &amp; Chart Area</div><div class="brand">PLAYNOVA</div>
  <div class="box c-teal" style="left:60px;top:50px;width:200px;height:12px"></div>
  <div class="box c-pink" style="left:60px;top:75px;width:150px;height:12px"></div>
  <div class="box c-orange" style="left:60px;top:100px;width:250px;height:12px"></div>
  <div class="box c-lime" style="left:60px;top:125px;width:120px;height:12px"></div>
  <div class="box c-purple" style="left:60px;top:150px;width:180px;height:12px"></div>
  <div class="t" style="left:14px;top:52px">Art</div><div class="t" style="left:14px;top:77px">Music</div><div class="t" style="left:14px;top:102px">Games</div><div class="t" style="left:14px;top:127px">Science</div><div class="t" style="left:14px;top:152px">Reading</div>
</section>
<section class="slide">
  <div class="title">Table Area</div><div class="brand">PLAYNOVA</div>
  <svg class="box" style="left:14px;top:38px" width="366" height="156" viewBox="0 0 366 156" font-family="Poppins,sans-serif" font-size="6">
    <rect width="122" height="22" fill="#27b3c4"/><rect x="122" width="122" height="22" fill="#e8367c"/><rect x="244" width="122" height="22" fill="#c3d62b"/>
    <text x="10" y="14" fill="#fff">Basic</text><text x="132" y="14" fill="#fff">Plus</text><text x="254" y="14" fill="#fff">Pro</text>
    <g fill="#8a8a8a"><text x="10" y="40">Templates</text><text x="132" y="40">Templates</text><text x="254" y="40">Templates</text>
    <text x="10" y="64">Calendars</text><text x="132" y="64">Calendars</text><text x="254" y="64">Calendars</text>
    <text x="10" y="88">Games</text><text x="132" y="88">Games</text><text x="254" y="88">Games</text>
    <text x="10" y="112">Support</text><text x="132" y="112">Support</text><text x="254" y="112">Support</text></g>
    <g stroke="#e3e3e3"><path d="M0 48H366M0 72H366M0 96H366M0 120H366"/></g>
  </svg>
</section>
<section class="slide">
  <div class="title">Radial &amp; Chart Area</div><div class="brand">PLAYNOVA</div>
  <div class="t" style="left:14px;top:50px;width:180px">• Teachers 45%<br>• Parents 30%<br>• Schools 25%</div>
  <svg class="box" style="left:240px;top:50px" width="120" height="120" viewBox="0 0 120 120" fill="none" stroke-width="16">
    <circle cx="60" cy="60" r="44" stroke="#e3e3e3"/>
    <circle cx="60" cy="60" r="44" stroke="#27b3c4" stroke-dasharray="124 400" transform="rotate(-90 60 60)"/>
    <circle cx="60" cy="60" r="44" stroke="#e8367c" stroke-dasharray="83 400" stroke-dashoffset="-124" transform="rotate(-90 60 60)"/>
    <text x="44" y="64" font-family="Poppins,sans-serif" font-size="12" fill="#4a4a4a" stroke="none">75%</text>
  </svg>
</section>

<!-- Row 16 -->
<section class="slide">
  <div class="title">Pricing Structure</div><div class="brand">PLAYNOVA</div>
  <div class="box c-teal" style="left:14px;top:40px;width:116px;height:30px"></div><div class="h w" style="left:50px;top:51px">€9</div>
  <div class="box c-pink" style="left:139px;top:40px;width:116px;height:30px"></div><div class="h w" style="left:175px;top:51px">€19</div>
  <div class="box c-lime" style="left:264px;top:40px;width:116px;height:30px"></div><div class="h w" style="left:300px;top:51px">€29</div>
  <div class="t" style="left:24px;top:80px">• 10 templates<br>• Calendars<br>• Email help</div>
  <div class="t" style="left:149px;top:80px">• 50 templates<br>• Games<br>• Chat help</div>
  <div class="t" style="left:274px;top:80px">• All templates<br>• Slideshows<br>• Full support</div>
</section>
<section class="slide">
  <div class="title">Our Team</div><div class="brand">PLAYNOVA</div>
  <div class="ph warm" role="img" aria-label="Team member portrait" style="left:40px;top:50px;width:56px;height:56px;border-radius:50%"></div>
  <div class="ph cool" role="img" aria-label="Team member portrait" style="left:130px;top:50px;width:56px;height:56px;border-radius:50%"></div>
  <div class="ph" role="img" aria-label="Team member portrait" style="left:220px;top:50px;width:56px;height:56px;border-radius:50%"></div>
  <div class="ph green" role="img" aria-label="Team member portrait" style="left:310px;top:50px;width:56px;height:56px;border-radius:50%"></div>
  <div class="h" style="left:44px;top:116px">Lina Ross</div><div class="h" style="left:134px;top:116px">Marc Dale</div><div class="h" style="left:222px;top:116px">Sofia Lane</div><div class="h" style="left:314px;top:116px">Tom Berry</div>
</section>
<section class="slide">
  <div class="box c-lime" style="left:0;top:0;width:394px;height:214px"></div>
  <div class="ph warm" role="img" aria-label="Photo of a smiling boy" style="left:0;top:0;width:160px;height:214px"></div>
  <div class="h w" style="left:180px;top:40px;font-size:14px">Our Contacts</div>
  <div class="t w" style="left:180px;top:70px;width:200px;font-size:6px">12 Garden Lane, Brightford<br>+44 20 0000 0000<br>hello@playnova.example<br>www.playnova.example</div>
</section>

</main>
</body>
</html>
```